Wine label for boutique family-owned winery

We need a front wine label designed for Velmora, our small, family-owned, Oregon based winery . Velmora makes warm climate red blends with grapes sourced from SE Washington state, USA. We are a startup business with wines for 2013 and 2014.

The name Velmora comes from the Georgian language, and is short for Tobias, my father's name. The Georgians have an 5000-8000 year history of winemaking, out of which they give heartfelt toasts that celebrate kinship, family, and loved ones of the past and future.

The design can be of various aspect ratios, but should fit flatly on a bordeaux style wine bottle.
We would like this wine label to work for red wines, and be convertible to work with white wines with some simple background color changes. The preferred file format is Adobe Illustrator. This label will be digitally printed.

A couple wine labels that I like:
- 9 Lanterns
- brelvastudio.com/labels "amber"

I am including a file to show what the existing Velmora label looks like.
Updates

Project Deadline Extended
Reason: To give more time for designer revisions. We want the right design!

Target Market(s)

Direct sales through group tastings.
Professionals aged 30-65 with disposable income.
$35/bottle wine.

Industry/Entity Type

Boutique

Font styles to use
Serif
Decorative
Script

Requirements
Must have
• Rich and/or earthy tones (see link to "Amber" above)
• The text on the front label will include:
• The brand name- Velmora
• Vintage: 2013
• Wine name- Corvalé Blend
• AVA: Washington State
• (The specific information will vary, but we need room for those categories of text.)
Nice to have
• We'd like to convey the qualities of sincerity, trustworthiness, and being grounded. If it's possible to convey our philosophy of sharing wine with friends and family that would be great.
• We have an existing logo "Velmora" that has been attached as an SVG file.
• It is not required to include this logo, but if it works in your design, all the better.
Should not have
• Feature photographs or likenesses of photographs

```html
<!DOCTYPE html>
<html lang="en">
<head>
<meta charset="utf-8">
<title>Velmora – Corvalé Blend 2013 Front Label</title>
<link rel="stylesheet" href="https://fonts.googleapis.com/css2?family=Cinzel:wght@400;500&family=Cormorant+Garamond:wght@500&display=swap">
<style>
  :root {
    --linen: #eee8dd;
    --linen-shade: #e6dfd2;
    --wine-deep: #5e0c1f;
    --wine-mid: #8e1420;
    --wine-bright: #c5241f;
    --glass-pale: rgba(246, 222, 226, 0.55);
    --glass-soft: rgba(236, 196, 204, 0.30);
    --brand-red: #a81d26;
    --ink: #1b1515;
  }
  html, body {
    margin: 0;
    padding: 0;
    width: 1200px;
    height: 2390px;
    overflow: hidden;
    background: var(--linen);
  }
  .label {
    position: relative;
    width: 1200px;
    height: 2390px;
    background: radial-gradient(ellipse at 50% 40%, var(--linen) 55%, var(--linen-shade) 100%);
  }
  .label-wash {
    position: absolute;
    left: 68px;
    top: 111px;
    width: 1050px;
    height: 1500px;
  }
  .label-wash svg {
    display: block;
    width: 100%;
    height: 100%;
  }
  .glasses-illustration {
    position: absolute;
    left: 256px;
    top: 299px;
    width: 546px;
    height: 1058px;
    border-radius: 200px 200px 60px 60px;
    background: linear-gradient(160deg, var(--glass-pale) 0%, var(--glass-soft) 100%);
  }
  .brand-name {
    position: absolute;
    left: 0;
    width: 1200px;
    top: 1733px;
    margin: 0;
    text-align: center;
    font-family: "Cinzel", serif;
    font-weight: 500;
    font-size: 250px;
    line-height: 1;
    letter-spacing: 0.01em;
    color: var(--brand-red);
    transform: scaleX(0.62);
    transform-origin: 50% 0;
  }
  .wine-name {
    position: absolute;
    left: 0;
    width: 1200px;
    top: 2039px;
    margin: 0;
    text-align: center;
    font-family: "Cinzel", serif;
    font-weight: 400;
    font-size: 84px;
    line-height: 1;
    letter-spacing: 0.12em;
    text-transform: uppercase;
    color: var(--ink);
  }
  .appellation {
    position: absolute;
    left: 0;
    width: 1200px;
    top: 2141px;
    margin: 0;
    text-align: center;
    font-family: "Cormorant Garamond", serif;
    font-weight: 500;
    font-size: 78px;
    line-height: 1;
    letter-spacing: 0.03em;
    color: var(--ink);
  }
  .vintage {
    position: absolute;
    left: 0;
    width: 1200px;
    top: 2242px;
    margin: 0;
    text-align: center;
    font-family: "Cormorant Garamond", serif;
    font-weight: 500;
    font-size: 89px;
    line-height: 1;
    letter-spacing: 0.04em;
    font-variant-numeric: lining-nums;
    color: var(--ink);
  }
</style>
</head>
<body>
  <main class="label">
    <div class="label-wash" role="img" aria-label="Watercolour wash in deep wine reds">
      <svg viewBox="0 0 1050 1500" preserveAspectRatio="none" aria-hidden="true">
        <defs>
          <linearGradient id="wash" x1="1" y1="0" x2="0" y2="1">
            <stop offset="0" stop-color="var(--wine-deep)"/>
            <stop offset="0.5" stop-color="var(--wine-mid)"/>
            <stop offset="1" stop-color="var(--wine-bright)"/>
          </linearGradient>
        </defs>
        <path fill="url(#wash)" d="M0 0 H1050 V1460 L1010 1465 L900 1462 L780 1468 L700 1472 L590 1462 L540 1470 L470 1458 L440 1490 L400 1500 L370 1470 L300 1455 L240 1440 L120 1375 L0 1370 Z"/>
      </svg>
    </div>

    <div class="glasses-illustration" role="img" aria-label="Illustration of two clinking glasses of red wine"></div>

    <h1 class="brand-name">Velmora</h1>
    <p class="wine-name">Corvalé Blend</p>
    <p class="appellation">Washington State</p>
    <p class="vintage">2013</p>
  </main>
</body>
</html>
```